Belvane Home Inspection Needs an Eye Catching FLYER

We need a EYE CATCHING flyer that will be sent to thousands of realtors. Our Riverside/San Bernardino County Inspection company performs residential/light commercial inspections for potential home buyers. We hope the flyer can highlight the services performed and present a professional look for the company. The final design should leave realtors thinking Belvane Home Inspections is the #1 inspection company in the area.

Target Market(s)

Realtors, Home Buyers, Home Sellers, and Home Owners.

Industry/Entity Type

Home Inspection

Font styles to use
Sans Serif

Colors
0392cd
33a6d7
3276b5
eaeaea
000000
ffffff

Requirements
Must have
• Must have a list of services Provided:
• Exterior, Interior, Electrical, Plumbing, Roof, Heating/Air cooling, Structural, Appliances, and Mold/Dry Rot.
• Tag Line "We inspect homes like we're buying them ourselves."
• number: 951-284-6190 Domain: belvanechecks.com ,Email: milo@belvanechecks.com
Nice to have
• Let realtors know we follow National Guild of Property Examiners (NGPE) Standards of Practice (SoP)
• Veteran Owned and Operated
• Discounts from the flyer of 20%
• Discounts to all veterans and public service members.

```html
<!DOCTYPE html>
<html lang="en">
<head>
<meta charset="utf-8">
<title>Belvane Home Inspection Flyer</title>
<link href="https://fonts.googleapis.com/css2?family=Roboto:wght@500;700&family=Questrial&family=Lato:wght@400;700&display=swap" rel="stylesheet">
<style>
  :root{
    --sky:#3aa0dc;
    --navy:#0e6697;
    --title:#1270a2;
    --icon-grey:#606060;
    --band-grey:#6b6b6b;
    --ink:#222222;
    --white:#ffffff;
    --page:#ffffff;
  }
  *{margin:0;padding:0;box-sizing:border-box}
  html,body{width:1200px;height:1200px;overflow:hidden;background:var(--page)}
  .flyer{position:absolute;left:176px;top:0;width:848px;height:1200px;background:var(--white);overflow:hidden;font-family:'Lato',sans-serif;color:var(--ink)}
  .photo{position:absolute}
  .photo--house{left:0;top:0;width:344px;height:202px;background:linear-gradient(180deg,#b9c6e4 0%,#c9b8cf 40%,#4d5a78 62%,#c8ccd2 100%)}
  .photo--frame{left:0;top:207px;width:344px;height:304px;background:linear-gradient(180deg,#9cc7ef 0%,#d9c49a 45%,#c99a55 75%,#8d6142 100%)}
  .photo--hill{left:350px;top:207px;width:498px;height:304px;background:linear-gradient(180deg,#e6a35c 0%,#b08a6c 30%,#8f8a6a 55%,#5f7a4a 80%,#7d8a88 100%)}
  .accent-bar{position:absolute;top:511px;height:8px}
  .accent-bar--left{left:0;width:344px;background:var(--sky)}
  .accent-bar--right{left:350px;width:498px;background:var(--navy)}
  .headline{position:absolute;left:350px;top:0;width:498px;height:202px;background:var(--sky);color:var(--white);padding:26px 0 0 38px}
  .headline span{display:block;font-size:44px;line-height:55px;letter-spacing:.3px;white-space:nowrap}
  .headline .strong{font-family:'Roboto',sans-serif;font-weight:700}
  .headline .light{font-family:'Questrial',sans-serif;font-weight:400}
  .services-tab{position:absolute;left:0;top:534px;width:286px;height:49px}
  .services-tab span{position:absolute;left:42px;top:12px;color:var(--white);font-family:'Roboto',sans-serif;font-weight:500;font-size:21px;letter-spacing:.2px}
  .service{position:absolute;width:250px}
  .service .badge{position:absolute;left:0;width:70px;height:70px;border-radius:50%;background:var(--icon-grey)}
  .service .badge svg{position:absolute;left:15px;top:15px;width:40px;height:40px}
  .service h3{position:absolute;left:84px;top:-2px;font-family:'Lato',sans-serif;font-weight:400;font-size:17.5px;color:var(--title);white-space:nowrap}
  .service p{position:absolute;left:85px;top:19px;width:150px;font-size:13.8px;line-height:17.2px;color:var(--ink)}
  .brand{position:absolute;left:58px;top:1019px;width:146px;height:146px;border-radius:50%;border:5px solid var(--navy);display:flex;flex-direction:column;align-items:center;justify-content:center;text-align:center;font-family:'Lato',sans-serif;font-weight:700;color:var(--navy)}
  .brand .name{font-size:26px;line-height:30px}
  .brand .sub{font-size:11px;line-height:14px}
  .cert-seal{position:absolute;left:262px;top:1019px;width:146px;height:146px;border-radius:50%;background:#0d0d0d}
  .contact-phone{position:absolute;left:571px;top:1001px;width:277px;height:62px}
  .contact-phone .text{position:absolute;left:87px;top:16px;color:var(--white);font-family:'Lato',sans-serif;font-weight:700;font-size:21px;letter-spacing:.3px}
  .contact-phone svg.icon{position:absolute;left:59px;top:19px;width:24px;height:24px}
  .contact-web{position:absolute;left:452px;top:1066px;width:396px;height:98px}
  .contact-row{position:absolute;left:55px;display:flex;align-items:center;gap:16px;color:var(--white);font-family:'Lato',sans-serif;font-weight:700;font-size:20px}
  .contact-row svg{width:20px;height:20px;flex:none}
</style>
</head>
<body>
<main class="flyer">
  <div class="photo photo--house" role="img" aria-label="Photo of a finished two-storey suburban house with grey siding and a garage at dusk"></div>
  <header class="headline">
    <span class="strong">WE INSPECT HOMES</span>
    <span class="light">LIKE WE'RE BUYING</span>
    <span class="strong">THEM OURSELVES</span>
  </header>
  <div class="photo photo--frame" role="img" aria-label="Photo of a house under construction with wood sheathing and an unfinished roof"></div>
  <div class="photo photo--hill" role="img" aria-label="Photo of a winding paved trail up a rocky hilltop at sunset over the valley"></div>
  <div class="accent-bar accent-bar--left"></div>
  <div class="accent-bar accent-bar--right"></div>

  <div class="services-tab">
    <svg width="286" height="49" viewBox="0 0 286 49"><polygon points="0,0 272,0 286,49 0,49" fill="var(--navy)"/></svg>
    <span>SERVICES PROVIDED</span>
  </div>

  <section class="service" style="left:40px;top:612px">
    <div class="badge" style="top:7px"><svg viewBox="0 0 40 40" fill="none" stroke="#fff" stroke-width="1.6"><rect x="8" y="6" width="24" height="28"/><line x1="20" y1="6" x2="20" y2="34"/><line x1="11" y1="18" x2="17" y2="10"/><line x1="23" y1="18" x2="29" y2="10"/></svg></div>
    <h3>EXTERIOR</h3>
    <p>Walls, siding, patios, decks, walkways, garage door, exterior fixtures and outlets, windows and doors</p>
  </section>
  <section class="service" style="left:314px;top:612px">
    <div class="badge" style="top:7px"><svg viewBox="0 0 40 40" fill="none" stroke="#fff" stroke-width="1.6"><rect x="6" y="6" width="28" height="28"/><line x1="6" y1="18" x2="22" y2="18"/><line x1="22" y1="6" x2="22" y2="34"/><rect x="10" y="23" width="7" height="6"/><rect x="26" y="10" width="5" height="5"/></svg></div>
    <h3>INTERIOR</h3>
    <p>Walls, floors, drywall, attic space, finishes, windows, doors</p>
  </section>
  <section class="service" style="left:584px;top:612px">
    <div class="badge" style="top:7px"><svg viewBox="0 0 40 40" fill="none" stroke="#fff" stroke-width="1.6"><circle cx="20" cy="20" r="15"/><line x1="16" y1="8" x2="16" y2="14"/><line x1="24" y1="8" x2="24" y2="14"/><path d="M12 14h16v5a8 8 0 0 1-16 0z"/><line x1="20" y1="27" x2="20" y2="33"/></svg></div>
    <h3>ELECTRICAL</h3>
    <p>Outlets, light fixtures, switches, main panel, service entrance conductors</p>
  </section>

  <section class="service" style="left:40px;top:744px">
    <div class="badge" style="top:8px"><svg viewBox="0 0 40 40" fill="none" stroke="#fff" stroke-width="1.6"><path d="M6 10h12v6h10v6"/><path d="M6 14h8v6h10"/><line x1="6" y1="8" x2="6" y2="16"/><path d="M28 26c-2 3-3 5-3 6a3 3 0 0 0 6 0c0-1-1-3-3-6z"/></svg></div>
    <h3>PLUMBING</h3>
    <p>Water heater, visible piping throughout home, street meter, all exterior and interior faucets</p>
  </section>
  <section class="service" style="left:314px;top:744px">
    <div class="badge" style="top:8px"><svg viewBox="0 0 40 40" fill="none" stroke="#fff" stroke-width="1.6"><path d="M9 10h22l4 20H5z"/><line x1="7" y1="17" x2="33" y2="17"/><line x1="6" y1="24" x2="34" y2="24"/><line x1="15" y1="10" x2="13" y2="30"/><line x1="25" y1="10" x2="27" y2="30"/><line x1="20" y1="10" x2="20" y2="30"/></svg></div>
    <h3>ROOF</h3>
    <p>Eaves, gutters, downspouts, vents, chimneys and all vent stacks</p>
  </section>
  <section class="service" style="left:584px;top:744px">
    <div class="badge" style="top:8px"><svg viewBox="0 0 40 40" fill="none" stroke="#fff" stroke-width="1.6"><path d="M6 19L20 7l14 12"/><path d="M10 16v17h20V16"/><circle cx="20" cy="24" r="5"/><line x1="20" y1="17" x2="20" y2="31"/><line x1="13" y1="24" x2="27" y2="24"/></svg></div>
    <h3>HEATING/COOLING</h3>
    <p>Main furnace, oil/wood/pellet/gas stoves, ducting and balancing, A/C unit and lines</p>
  </section>

  <section class="service" style="left:40px;top:882px">
    <div class="badge" style="top:8px"><svg viewBox="0 0 40 40" fill="none" stroke="#fff" stroke-width="1.6"><circle cx="20" cy="7" r="3"/><line x1="20" y1="10" x2="20" y2="16"/><line x1="10" y1="16" x2="30" y2="16"/><line x1="10" y1="16" x2="10" y2="22"/><line x1="30" y1="16" x2="30" y2="22"/><line x1="20" y1="16" x2="20" y2="22"/><circle cx="10" cy="25" r="3"/><circle cx="20" cy="25" r="3"/><circle cx="30" cy="25" r="3"/><line x1="4" y1="32" x2="36" y2="32"/></svg></div>
    <h3>STRUCTURAL</h3>
    <p>Foundation, framing, roof , walls, sill plate, landscape swale, crawlspace and attic</p>
  </section>
  <section class="service" style="left:314px;top:882px">
    <div class="badge" style="top:8px"><svg viewBox="0 0 40 40" fill="none" stroke="#fff" stroke-width="1.6"><rect x="8" y="5" width="24" height="30" rx="2"/><line x1="8" y1="12" x2="32" y2="12"/><circle cx="20" cy="23" r="7"/><circle cx="20" cy="23" r="3"/></svg></div>
    <h3>APPLIANCES</h3>
    <p>Dishwasher, ranges, refrigerators, waste disposal, laundry facilities, microwave</p>
  </section>
  <section class="service" style="left:584px;top:882px">
    <div class="badge" style="top:8px"><svg viewBox="0 0 40 40" fill="none" stroke="#fff" stroke-width="1.6"><rect x="10" y="8" width="20" height="20"/><line x1="15" y1="8" x2="15" y2="28"/><line x1="20" y1="8" x2="20" y2="28"/><line x1="25" y1="8" x2="25" y2="28"/><line x1="6" y1="28" x2="34" y2="28"/><line x1="6" y1="33" x2="34" y2="33"/></svg></div>
    <h3>MOLD/DRY ROT</h3>
    <p>lorem ipsumlorem ipsum lorem ipsum lorem lorem lorem ipsumipsum</p>
  </section>

  <div class="brand">
    <span class="name">Belvane</span>
    <span class="sub">Home Inspections</span>
  </div>
  <div class="cert-seal" role="img" aria-label="National Guild of Property Examiners membership seal"></div>

  <div class="contact-phone">
    <svg width="277" height="62" viewBox="0 0 277 62"><polygon points="30,0 277,0 277,62 0,62" fill="var(--navy)"/></svg>
    <svg class="icon" viewBox="0 0 24 24"><path fill="#fff" d="M6.6 10.8a15.1 15.1 0 0 0 6.6 6.6l2.2-2.2a1 1 0 0 1 1-.25 11.4 11.4 0 0 0 3.6.57 1 1 0 0 1 1 1V20a1 1 0 0 1-1 1A17 17 0 0 1 3 4a1 1 0 0 1 1-1h3.5a1 1 0 0 1 1 1c0 1.25.2 2.45.57 3.57a1 1 0 0 1-.25 1z"/></svg>
    <span class="text">951-284-6190</span>
  </div>

  <div class="contact-web">
    <svg width="396" height="98" viewBox="0 0 396 98" style="position:absolute;left:0;top:0"><polygon points="42,0 396,0 396,98 0,98" fill="var(--band-grey)"/></svg>
    <div class="contact-row" style="top:14px">
      <svg viewBox="0 0 20 20" fill="none" stroke="#fff" stroke-width="1.4"><circle cx="10" cy="10" r="8"/><ellipse cx="10" cy="10" rx="3.5" ry="8"/><line x1="2" y1="10" x2="18" y2="10"/><line x1="3.5" y1="6" x2="16.5" y2="6"/><line x1="3.5" y1="14" x2="16.5" y2="14"/></svg>
      <span>www.belvanechecks.com</span>
    </div>
    <div class="contact-row" style="top:54px">
      <svg viewBox="0 0 20 20" fill="none" stroke="#fff" stroke-width="1.4"><rect x="1.5" y="4" width="17" height="12"/><path d="M1.5 4l8.5 7 8.5-7"/></svg>
      <span>milo@belvanechecks.com</span>
    </div>
  </div>
</main>
</body>
</html>
```